Redesign Of Hotel Coupon/Voucher 8.5 x 11

I would like to redesign my voucher.

Please provide me a color flyer design but one that would be easy on printing costs...for example printing from home computer/printer.

I would like to see some color designs...maybe some black and white and also full graphics and even basic like the plum tally voucher I provided as a sample. The 2 night hotel stay is the voucher I need to redesign...

Target Market(s)

Consumers

Industry/Entity Type

Hotel

Requirements
Must have
• exact text in current designs---look official, credible and trust worthy
Nice to have
• I would like to redesign my voucher.
• Please provide me a color flyer design but one that would be easy on printing costs...for example printing from home computer/printer.
• I would like to see some color designs...maybe some black and white and also full graphics and even basic like the plum tally voucher I provided as a sample. The 2 night hotel stay is the voucher I need to redesign...
Should not have

```html
<!DOCTYPE html>
<html lang="en">
<head>
<meta charset="utf-8">
<title>2 Night Hotel Stay Certificate</title>
<link href="https://fonts.googleapis.com/css2?family=Lato:wght@400;700;900&family=Teko:wght@500&display=swap" rel="stylesheet">
<style>
:root{
  --orange:#f26f21;
  --blue:#1a9ee0;
  --ink:#2a2a2a;
  --dark:#242424;
  --paper:#ffffff;
  --bg:#e4e4e4;
  --line:#555;
}
*{box-sizing:border-box;margin:0;padding:0}
html,body{width:1200px;height:1200px;overflow:hidden;background:var(--bg);font-family:"Lato",sans-serif;color:var(--ink)}
.sheet{position:absolute;left:175px;top:50px;width:850px;height:1100px;background:var(--paper);box-shadow:0 6px 24px rgba(0,0,0,.18);overflow:hidden}
.hero{position:absolute;left:28px;top:30px;width:794px;height:250px;border:5px solid var(--orange);border-right-width:12px;clip-path:polygon(0 0,100% 0,100% 100%,30% 100%,25% 78%,0 78%)}
.hero-photo{position:absolute;inset:0;background:linear-gradient(100deg,#f4f6f8 0 14%,#dfe8ee 14% 24%,#7fc6ea 24%,#2f9fd9 55%,#6ec3ee 80%,#dff1fb)}
.compliments{position:absolute;right:18px;top:62px;width:200px;height:200px;background:var(--orange);clip-path:polygon(12% 0,100% 0,100% 100%,12% 100%,0 50%);color:#fff;text-align:center;font-weight:700;font-size:14px;line-height:1.2;padding:36px 10px 0 30px;text-transform:uppercase;box-shadow:0 0 0 4px #fff}
.compliments p+p{margin-top:18px}
.title{position:absolute;left:30px;top:236px;font-family:"Teko",sans-serif;font-weight:500;font-size:40px;color:var(--blue);letter-spacing:.5px;line-height:1}
.destinations{position:absolute;left:30px;top:290px;width:790px;font-size:10.5px;font-weight:700;line-height:1.3}
.tc-tab{position:absolute;left:30px;top:394px;background:var(--orange);color:#fff;font-weight:900;font-size:13px;padding:4px 14px;clip-path:polygon(0 0,92% 0,100% 100%,0 100%)}
.terms{position:absolute;left:30px;top:424px;width:790px;font-size:10.6px;font-weight:700;line-height:1.4;text-align:justify}
.divider{position:absolute;left:0;top:772px;width:850px;height:4px;background:var(--orange)}
.redeem{position:absolute;left:28px;top:786px;width:220px;height:290px}
.redeem svg{position:absolute;inset:0}
.redeem-text{position:absolute;left:16px;top:14px;width:190px;color:#fff;font-size:10px;font-weight:700;line-height:1.25}
.redeem-text h3{color:var(--orange);font-size:11.5px;margin-top:8px}
.redeem-text .id{color:var(--blue);font-size:11.5px;margin-top:8px;font-weight:900}
.form{position:absolute;font-size:10px;font-weight:700}
.form h2{color:var(--blue);font-size:12px;font-weight:900;margin-bottom:6px;text-transform:uppercase}
.field{display:flex;align-items:flex-end;height:16px}
.field span{white-space:nowrap;margin-right:6px}
.field i{flex:1;border-bottom:1px solid var(--line);height:10px}
.billing{left:266px;top:790px;width:170px}
.shipping{left:266px;top:946px;width:170px}
.payment{left:470px;top:796px;width:350px}
.payment h2{margin-bottom:0}
.payment .method{color:var(--blue);font-size:11px;font-weight:900;margin-bottom:10px}
.options{display:grid;grid-template-columns:90px 1fr;row-gap:2px;margin-bottom:12px}
.options label::before{content:"";display:inline-block;width:8px;height:8px;border:1px solid var(--ink);border-radius:50%;margin-right:5px;vertical-align:-1px}
.card .field{width:260px}
.agree{position:absolute;left:470px;top:946px;width:340px}
.agree h2{color:var(--blue);font-size:13px;font-weight:900;line-height:1.2}
.agree .sign{border-bottom:1px solid var(--line);height:22px;width:240px}
.note{margin:8px 0 0 100px;width:240px;font-size:8.8px;font-weight:700;line-height:1.25;text-align:justify}
.band-orange{position:absolute;left:0;top:1072px;width:260px;height:12px;background:var(--orange);clip-path:polygon(0 0,100% 0,95% 100%,0 100%)}
.band-blue{position:absolute;left:250px;top:1080px;width:600px;height:20px;background:var(--blue);clip-path:polygon(3% 0,100% 0,100% 100%,0 100%)}
</style>
</head>
<body>
<div class="sheet">
  <div class="hero">
    <div class="hero-photo" role="img" aria-label="Photo of a white seaside terrace with lounge chairs overlooking a blue sea"></div>
  </div>
  <div class="compliments">
    <p>The certificate is compliments of</p>
    <p>Name<br>Phone Number<br>E-mail Address</p>
  </div>
  <h1 class="title">2 NIGHT HOTEL STAY</h1>

  <p class="destinations">Destinations Available: Anaheim, CA--Atlanta, GA--Atlantic City, NJ--Branson, MO--Cancun, MX--Charleston, SC--Coeur d' Alene, ID--Daytona Beach, FL--Destin, FL--Ft. Lauderdale, FL--Ft. Meyers, FL--Gatlinburg, TN--Hilton Head, SC--Honolulu, HI--Kissimmee, FL--Lake Tahoe, CA--Las Vegas, NV--Myrtle Beach, SC--Niagara Falls/Buffalo Area, NY--Orlando, FL--Ormond Beach, FL--Palm Springs, CA--Pigeon Forge, TN--St. Petersburg, FL--San Antonio, TX--San Diego, CA--San Francisco, CA--Sedona, AZ--Sonoma Wine Country, CA--St. George, UT--Tampa, FL--Williamsburg, VA--Wisconsin Dells, WI--Tallahassee, FL--Augusta, GA--Columbia, SC--New York, NY--Florence, SC--Washington, D.C.--Chicago, IL--Salt Lake City, UT--Hollywood, CA--Dayton, OH--Tucson, AZ--Niagra Falls, ON/CAN--Seattle, WA--Portland, OR--Antioch, CA--San Mateo, CA--Brunswick, GA--Nashville, TN</p>

  <div class="tc-tab">TERMS &amp; CONDITIONS</div>
  <p class="terms">This certificate will be considered void if bartered or purchased for legal tender by the recipient. This certificate is valid for a reservation request form offering 2 adults 21 years of age and older plus up to 2 children under the age of 18, 2 nights of hotel accommodations in the city of their choice of available cities. The cost to activate this certificate to receive the reservation request form is just a one-time non-refundable $14.95 processing fee. The cost upon requesting reservations is just a tax &amp; fee deposit of $33 per night. Taxes &amp; fees usually range from $12-$33 per night depending on when and where you travel to. If the taxes &amp; fees are less than the $33 per night the difference will be refunded after travel is completed. 30 days advance reservation notice is required. In order to guarantee that you will show up to your booked reservation you will be required to pay a REFUNDABLE $50 "Reservation Guarantee Deposit". If you send in your travel dates, etc and you do not end up traveling then the reservation guarantee deposit will not be refundable. 7 days before and after holidays and conventions are not available. This offer is valid 7 days a week subject to availability. Friday and Saturday nights will require a surcharge of $20 per night. A $5 per person per night surcharge is enforced for each child up to 2 children under the age of 18. This offer is not valid for group travel. The recipient of this certificate is responsible for all expenses including but not limited to: transfers, food, gratuities, all pertinent fees, taxes, hotel surcharges, resort fees and any other miscellaneous expenses. If you activate this certificate online you will be able to instantly print your reservation request form. If you cannot print your own reservation request form we will mail it to you. You should receive it in the mail within 14 days. This certificate cannot be combined with any other promotional vacation offer. The expiration date on this certificate pertains only to activation of this certificate and not actual travel. You must activate this certificate by the expiration date printed on this certificate in order to receive the reservation request form. You must fill out the reservation request form with your destination choices and arrival dates and mail it to our fulfillment department within 6 months after activation, however travel can be completed within 12 months after activation. You will be required to give the travel agency multiple arrival dates and destinations. Only one 2 Night Hotel certificate Per Household Per Year. This certificate has no cash surrender value, void if discontinued and where prohibited by law. The terms of this offer are subject to change without notice. Do not rely upon representations other than what is printed on this certificate or the reservation request form. CST # 4417302</p>

  <div class="divider"></div>

  <div class="redeem">
    <svg width="220" height="290" viewBox="0 0 220 290" aria-hidden="true">
      <polygon points="4,4 216,4 216,256 110,286 4,256" fill="var(--dark)" stroke="var(--blue)" stroke-width="5"/>
    </svg>
    <div class="redeem-text">
      <p>Simply fill out the form on this certificate and enclose payment of U.S. $14.95. Credit Card, Charge Card, Travel Card, Debit Card, Check Card, Check &amp; Money Orders are all accepted.</p>
      <h3>3 Ways To Redeem:</h3>
      <p>1. For expedited redemption go to: www.StayPerksForYou.com<br>2. Fax* certificate to: 1-888-555-0142</p>
      <h3>3. Mail* to:</h3>
      <p>Redemption Center<br>4120 Harbor View Rd Ste B #210<br>Lakeview, Ca 90000</p>
      <p class="id">Certificate ID: -10002<br>Expiration Date: 04/08/2017</p>
    </div>
  </div>

  <div class="form billing">
    <h2>Billing Information</h2>
    <div class="field"><span>Name:</span><i></i></div>
    <div class="field"><span>Address:</span><i></i></div>
    <div class="field"><span>City:</span><i></i></div>
    <div class="field"><span>State:</span><i></i></div>
    <div class="field"><span>Zip Code:</span><i></i></div>
    <div class="field"><span>Country:</span><i></i></div>
    <div class="field"><span>Phone:</span><i></i></div>
    <div class="field"><span>Email:</span><i></i></div>
  </div>

  <div class="form shipping">
    <h2>Shipping Information</h2>
    <div class="field"><span>Name:</span><i></i></div>
    <div class="field"><span>Address:</span><i></i></div>
    <div class="field"><span>City:</span><i></i></div>
    <div class="field"><span>State:</span><i></i></div>
    <div class="field"><span>Zip Code:</span><i></i></div>
    <div class="field"><span>Country:</span><i></i></div>
  </div>

  <div class="form payment">
    <h2>Payment Information</h2>
    <p class="method">Payment Method:</p>
    <div class="options">
      <label>Check</label><label>Check Money Order</label>
      <label>Credit</label><label>Charge Card</label>
      <label>Travel</label><label>Debit Card</label>
    </div>
    <div class="card">
      <div class="field"><span>Name On Card:</span><i></i></div>
      <div class="field"><span>Card # (16 digits):</span><i></i></div>
      <div class="field"><span>Expiration Date</span><i></i></div>
    </div>
  </div>

  <div class="agree">
    <h2>I agree to terms and conditions<br>Signature:</h2>
    <div class="sign"></div>
    <p class="note">"Redemption Center" will appear on your billing statement. Make checks and money orders payable to: "Redemption Center" * You will receive your information by mail within 10 days. ** Last 3 digits on back of card (4 digits on front of some cards).</p>
  </div>

  <div class="band-orange"></div>
  <div class="band-blue"></div>
</div>
</body>
</html>
```